【 概要 】 ホームページのTOP画像のデザインを募集いたします。 飲食店専用ホームページ制作です。 メインターゲットは飲食店オーナーの方々です。 飲食のホームページにあった「どんなお店なのか」、「どんなメニュ・どんなコースがあるか」など、 そのお店を気になった方々に来店を促すようなTOP画像が希望です。 【 依頼内容 】 ・サイズ:1920px×1080px ・作成数: 1種類 ・利用用途:ホームページトップ画像 ・色:オレンジ/赤/黄色 ・文言:あなたのお店をオリジナルデザインで作ってみませんか? 【 デザインイメージ 】 ・雰囲気:信頼感、安心感があり、ポップ感 ・現在制作途中のホームページにあった感じ http://sampwebnoren.com/ ・参考他社デザイン https://www.hanamuraya.co.jp/menu/kikaku/ また飲食以外も対象にしたいと思ったので別案も制作していただけたら幸いです。 【 依頼内容 】 色:グレー/白/黒 文言:ホームページはオリジナルデザインで! 参考URL:https://qv-webworks.jp/hp/?utm_source=kensaku&utm_medium=cpc&qclid=QRS.2004815367.PXbTwLcdFhZNruqk5p8w27AKRGetSd3hvm-qWFBCZjBXFgKQ5_E_CzX 【 契約金額(税抜) 】 1万円 ※契約金額(税込)からシステム利用料を差し引いた金額が、ワーカーさまの受取金額となります その他ご質問等ありましたら、気軽にお問い合わせください。 ご応募をお待ちしております! |
| https://www.hanamuraya.co.jp/menu/kikaku/ | ||
私共の内容をよく理解していただいた上で作成していただきありがとうございます。
今回korunote様のご提案が弊社のHPの表画面での使用に一番最適だと考え作用させていただきます。
皆様色々ご提案ありがとうございます。とても素敵なデザインを見していただきました。
弊社は今後よくご依頼などをさせていただきますので、その際は皆様また力を貸していただければと思います。

```html
<!DOCTYPE html>
<html lang="ja">
<head>
<meta charset="UTF-8">
<title>あなたのお店をオリジナルデザインで作ってみませんか?</title>
<link rel="stylesheet" href="https://fonts.googleapis.com/css2?family=M+PLUS+Rounded+1c:wght@700;800;900&display=swap">
<style>
  :root {
    --stripe-yellow: #f8d64e;
    --stripe-pink: #e63a72;
    --oval-fill: #f2dfbf;
    --oval-border: #8b5a2b;
    --oval-inner: #b98a55;
    --text-brown: #4e3219;
    --accent-red: #e5322b;
    --white: #ffffff;
    --figure-light: #fbf1e2;
    --figure-mid: #f3d9b3;
  }
  * { margin: 0; padding: 0; box-sizing: border-box; }
  html, body {
    width: 1200px;
    height: 674px;
    overflow: hidden;
    background: var(--white);
  }
  .hero {
    position: relative;
    width: 1200px;
    height: 674px;
    overflow: hidden;
    font-family: "M PLUS Rounded 1c", sans-serif;
    background: repeating-linear-gradient(
      180deg,
      var(--stripe-yellow) 0px,
      var(--stripe-yellow) 26px,
      var(--stripe-pink) 26px,
      var(--stripe-pink) 80px,
      var(--stripe-yellow) 80px,
      var(--stripe-yellow) 114px
    );
  }
  .figure {
    position: absolute;
    z-index: 1;
    background: linear-gradient(160deg, var(--figure-light), var(--figure-mid));
    border-radius: 90px 90px 24px 24px;
  }
  .figure--top-left     { left: 40px;  top: 0;     width: 210px; height: 264px; border-radius: 0 0 60px 60px; }
  .figure--top-right    { left: 900px; top: 44px;  width: 270px; height: 206px; }
  .figure--bottom-left  { left: 50px;  top: 384px; width: 240px; height: 290px; }
  .figure--bottom-right { left: 920px; top: 410px; width: 250px; height: 264px; }

  .badge {
    position: absolute;
    z-index: 2;
    left: 214px;
    top: 136px;
    width: 776px;
    height: 414px;
    border-radius: 50%;
    background: var(--oval-fill);
    border: 9px solid var(--oval-border);
    box-shadow: inset 0 0 0 5px var(--oval-fill), inset 0 0 0 8px var(--oval-inner);
  }
  .badge__lead,
  .badge__title,
  .badge__tail {
    position: absolute;
    left: 0;
    width: 100%;
    text-align: center;
    white-space: nowrap;
    line-height: 1;
  }
  .badge__lead {
    top: 43px;
    font-size: 46px;
    font-weight: 800;
    color: var(--text-brown);
    letter-spacing: 1px;
  }
  .badge__lead .shop-mark {
    display: inline-block;
    width: 40px;
    height: 42px;
    margin: 0 4px;
    vertical-align: -4px;
    background: var(--white);
    border: 3px solid var(--text-brown);
    border-radius: 6px;
  }
  .badge__lead .tick {
    display: inline-block;
    width: 4px;
    height: 30px;
    margin: 0 10px;
    vertical-align: 2px;
    border-radius: 2px;
    background: var(--text-brown);
  }
  .badge__lead .tick--left  { transform: rotate(-30deg); }
  .badge__lead .tick--right { transform: rotate(30deg); }
  .badge__title {
    top: 140px;
    font-size: 70px;
    font-weight: 900;
    color: var(--accent-red);
    letter-spacing: 1px;
    -webkit-text-stroke: 14px var(--white);
    paint-order: stroke fill;
  }
  .badge__rule {
    position: absolute;
    left: 78px;
    top: 230px;
    width: 602px;
    height: 6px;
    border-radius: 3px;
    background: var(--accent-red);
  }
  .badge__tail {
    top: 258px;
    font-size: 42px;
    font-weight: 800;
    color: var(--text-brown);
    letter-spacing: 1px;
  }
</style>
</head>
<body>
  <main class="hero">
    <div class="figure figure--top-left" role="img" aria-label="おたまを持った頭巾とエプロン姿の女性店員のイラスト"></div>
    <div class="figure figure--top-right" role="img" aria-label="ビールジョッキを掲げる頭巾姿の男性店員のイラスト"></div>
    <div class="figure figure--bottom-left" role="img" aria-label="湯気の立つマグカップを持つニット帽の店員のイラスト"></div>
    <div class="figure figure--bottom-right" role="img" aria-label="コーヒーサーバーを持つ巻き髪の店員のイラスト"></div>

    <section class="badge">
      <h1 class="badge__lead"><span class="tick tick--left"></span>あなたのお店<span class="shop-mark" role="img" aria-label="コック帽をかぶったお店のアイコン"></span>を<span class="tick tick--right"></span></h1>
      <p class="badge__title">オリジナルデザイン</p>
      <div class="badge__rule"></div>
      <p class="badge__tail">で作ってみませんか?</p>
    </section>
  </main>
</body>
</html>
```